Logo + Label Design (Men’s Grooming Brand & Product Packaging)

Design a logo and 2 oz pomade label for Brant, a modern men’s grooming brand focused on clean, high-quality, natural ingredients. The design should establish a bold, masculine, minimalist identity that can later extend to products like shaving gel and body wash.

Key Requirements

Create a primary logo for “Brant” and a core label for the 2 oz pomade jar (screw-top).

Use a clean, modern style — masculine, confident, and approachable (think Wendel’s, Valto, Northfield Mill).

Design for 1–2 color screen printing on solid jar colors (white, black, or navy).

Avoid gradients, foil, or embossing. Must work in black & white.

Provide: vector logo, mockup of the 2 oz jar, color palette (CMYK/RGB/HEX), and font specs.

Winning design may lead to future projects (body wash, shave gel, skincare lines).

Font styles to use
Other font styles liked:
• We like the fonts and design concept in the attached mockup.

Requirements
Should not have
• We want to avoid too much writing or busy designs. We want to avoid having graphics/illustrations embedded in the logo if they will cause the brand to look less classy or sophisticated. We also want the design to look simple and all-American (e.g. Pellham and Stroud, Tall Pine, The BRIM, etc). We’d like to give a Kessler & Dunmore vibe that feels classy and high end.

```html
<!DOCTYPE html>
<html lang="en">
<head>
<meta charset="utf-8">
<title>Brant Hair Pomade – Jar Label</title>
<link href="https://fonts.googleapis.com/css2?family=Lato:wght@400;700;900&family=Source+Sans+3:wght@400;600&display=swap" rel="stylesheet">
<style>
  :root {
    --navy: #3b4276;
    --white: #ffffff;
    --paper: #f1f0ee;
  }
  * { margin: 0; padding: 0; box-sizing: border-box; }
  html, body { width: 1200px; height: 912px; overflow: hidden; background: var(--paper); }
  .canvas { position: relative; width: 1200px; height: 912px; }

  .lid-label {
    position: absolute; left: 310px; top: 30px;
    width: 580px; height: 580px; border-radius: 50%;
    background: var(--navy); color: var(--white);
    font-family: "Lato", sans-serif; text-align: center;
    overflow: hidden;
  }
  .lid-ring {
    position: absolute; inset: 14px; border-radius: 50%;
    border: 3px solid var(--white);
  }
  .brand-name {
    position: absolute; top: 118px; left: 0; right: 0;
    font-weight: 900; font-size: 108px; letter-spacing: 2px; line-height: 1;
  }
  .product-name {
    position: absolute; top: 262px; left: 0; right: 0;
    font-weight: 900; font-size: 42px; letter-spacing: 1.5px; line-height: 1.1;
  }
  .scent {
    position: absolute; top: 318px; left: 0; right: 0;
    font-weight: 400; font-size: 34px; letter-spacing: 1.5px; line-height: 1.1;
  }
  .divider {
    position: absolute; top: 372px; left: 90px; right: 90px;
    height: 2px; background: var(--white);
  }
  .hold-finish {
    position: absolute; top: 390px; left: 0; right: 0;
    font-weight: 900; font-size: 23px; letter-spacing: 1px; line-height: 1.1;
  }
  .net-weight {
    position: absolute; top: 470px; left: 0; right: 0;
    font-weight: 700; font-size: 24px; line-height: 1.1;
  }

  .side-label {
    position: absolute; left: 150px; top: 650px;
    width: 900px; height: 232px;
    background: var(--navy); color: var(--white);
    font-family: "Source Sans 3", sans-serif;
  }
  .info-box {
    position: absolute; left: 150px; top: 22px; width: 600px; height: 140px;
    border: 1.5px solid var(--white);
    display: flex; gap: 34px; padding: 14px 18px;
    font-size: 16px; line-height: 1.3;
  }
  .info-col { flex: 1; }
  .info-col h3 { font-size: 16px; font-weight: 600; }
  .maker {
    position: absolute; left: 0; right: 0; top: 172px;
    text-align: center; font-size: 15px; line-height: 1.35;
  }
</style>
</head>
<body>
<div class="canvas">
  <div class="lid-label">
    <div class="lid-ring"></div>
    <div class="brand-name">BRANT</div>
    <div class="product-name">HAIR POMADE</div>
    <div class="scent">FRESH &amp; CLEAN</div>
    <div class="divider"></div>
    <div class="hold-finish">MEDIUM HOLD – MATTE FINISH</div>
    <div class="net-weight">NET WT 2oz (57gm)</div>
  </div>

  <div class="side-label">
    <div class="info-box">
      <div class="info-col">
        <h3>Directions:</h3>
        <p>Work a small amount between your palms and apply evenly through dry or damp hair. Style as desired.</p>
      </div>
      <div class="info-col">
        <h3>Ingredients:</h3>
        <p>Beeswax, Shea Butter, Jojoba Oil, Coconut Oil, Fragrance, Natural Extracts and other conditioning agents.</p>
      </div>
    </div>
    <div class="maker">
      Manufactured by: Harbor Line Grooming Co.<br>
      Kingston, Canada - www.harborlinegrooming.com
    </div>
  </div>
</div>
</body>
</html>
```